Homepage Redesign - Hi-tech business Law Firm

I'm looking for an updated graphic design (pdf file) for the homepage of dorvantlegal.ca (and which will form the general template of the other pages - but you don't need to design that). Detailed specs are in the Word file.

Deliverable is 1 pdf file that I find good looking, that sets forth the layout of the new page.

Target Market(s)

Sophisticated customers

Industry/Entity Type

Legal

Number of Pages Required

1 page

Requirements
Nice to have
• For a main background, tech type images to do with high powered boardrooms, computers, graphs, numbers, high tech manufacturing lines etc. Also, I tend to like blues and light greys, and uploaded a file today that shows my generally preferred layout, which a few of you have been getting close to.
Should not have
• Any mention of 'Personal Injury,' backgrounds that include books, or buildings with roman columns. Page should not be in dark colors or harsh on the eyes.

```html
<!DOCTYPE html>
<html lang="en">
<head>
<meta charset="utf-8">
<title>Dorvant Legal — Homepage</title>
<link href="https://fonts.googleapis.com/css2?family=Inter:wght@300;400;500;600;700;800&display=swap" rel="stylesheet">
<style>
:root{
  --navy:#0c3b5e;
  --navy-deep:#082a45;
  --blue:#1e6c9e;
  --ink:#1b1b1b;
  --grey-bg:#ececec;
  --light-blue:#e6edf3;
  --footer-bg:#eef2f6;
  --field:#f1f2f4;
  --muted:#555;
  --star:#f4a51c;
}
*{box-sizing:border-box;margin:0;padding:0}
html,body{width:1200px;height:4615px;overflow:hidden}
body{font-family:"Inter",sans-serif;color:var(--ink);background:#fff;position:relative}
.abs{position:absolute}
section,header,footer,.band{position:absolute;left:0;width:1200px}
.center{text-align:center}

/* top bar */
.topbar{top:0;height:32px;background:var(--navy-deep);color:#fff;font-size:11px;font-weight:500}
.topbar span{position:absolute;top:9px;display:flex;align-items:center;gap:6px}
/* header */
.site-header{top:32px;height:81px;background:#fff}
.logo{display:flex;align-items:center;gap:8px}
.logo .mark{width:32px;height:32px;background:var(--navy)}
.logo .name{font-size:13px;font-weight:600;letter-spacing:2px;color:var(--navy);line-height:1.1}
.nav{position:absolute;left:386px;top:35px;display:flex;gap:16px;font-size:10.5px;color:#333}
.search{position:absolute;left:876px;top:25px;width:160px;height:32px;border:1px solid #ccc;border-radius:16px;font-size:9px;color:#999;padding:10px 16px}

/* hero */
.hero{top:113px;height:553px;background:linear-gradient(90deg,#111 0%,#1d1f22 55%,#2a2d31 100%);overflow:hidden}
.hero-photo{position:absolute;left:107px;top:30px;width:430px;height:523px;background:radial-gradient(ellipse at 50% 40%,#4a5866 0%,#2a3440 55%,#1b1d20 100%)}
.hero-deco{position:absolute;left:800px;top:0;width:400px;height:340px;background:radial-gradient(circle at 60% 40%,rgba(120,130,140,.25),rgba(0,0,0,0) 70%)}
.hero-copy{position:absolute;left:613px;top:150px;color:#fff}
.hero-copy .kicker{font-size:37px;font-weight:300;color:var(--blue);letter-spacing:1px;line-height:1}
.hero-copy h1{font-size:37px;font-weight:800;line-height:1.03;margin-top:4px}
.btn{display:inline-block;border-radius:20px;font-size:12.5px;font-weight:700;color:#fff;text-align:center;line-height:38px;height:38px}
.hero .btn-read{position:absolute;left:613px;top:324px;width:188px;background:var(--navy)}
.hero .btn-video{position:absolute;left:806px;top:324px;width:193px;background:#7d7f82}
.dots{position:absolute;left:620px;top:444px;display:flex;gap:8px;align-items:center}
.dots i{width:14px;height:14px;border-radius:50%;background:#777;display:block}
.dots i.on{width:20px;height:20px;background:#fff}

/* badges */
.badges{top:666px;height:147px;background:var(--navy)}
.badge-plain{position:absolute;top:46px;height:48px;background:rgba(255,255,255,.16);border-radius:4px}
.badge-text{position:absolute;left:721px;top:46px;width:260px;font-size:9.5px;color:#fff;line-height:1.4}

/* evaluation */
.evaluation{top:813px;height:853px}
.sec-title{font-size:31px;font-weight:700;text-align:center;letter-spacing:.5px}
.rule{width:68px;height:2px;background:var(--navy);margin:10px auto 0}
.form-box{position:absolute;left:211px;top:247px;width:778px;height:497px;border:1px solid #cfcfcf;border-radius:26px}
.field{position:absolute;background:var(--field);border-radius:22px;font-size:11.5px;color:#888;padding:14px 30px}
.consent{position:absolute;left:67px;top:345px;font-size:10px;color:#333}
.consent b{color:var(--navy)}
.send{position:absolute;left:67px;top:382px;width:646px;height:52px;border-radius:26px;background:var(--navy);color:#fff;font-weight:700;font-size:14px;text-align:center;line-height:52px}

/* experience */
.experience{top:1666px;height:994px;background:var(--grey-bg)}
.exp-head{position:absolute;top:100px;width:100%;text-align:center}
.exp-head h2{font-size:31px;font-weight:800;line-height:1.07}
.exp-head h3{font-size:23px;font-weight:700;color:var(--navy);margin-top:6px;letter-spacing:.5px}
.exp-rule{position:absolute;left:226px;top:229px;width:764px;height:1px;background:#aaa}
.exp-copy{position:absolute;left:200px;top:262px;width:800px;text-align:center;font-size:10.5px;line-height:1.7;color:#333}
.exp-copy p+p{margin-top:14px}
.news-card{position:absolute;top:447px;width:280px;height:434px;background:var(--navy);border-radius:4px;color:#fff;text-align:center}
.news-card .thumb{position:absolute;left:8px;top:8px;width:264px;height:167px}
.news-card .date{position:absolute;left:90px;top:194px;width:100px;height:20px;border-radius:10px;background:#3f6685;font-size:10px;line-height:20px}
.news-card h4{position:absolute;left:18px;top:226px;width:244px;font-size:15.5px;font-weight:700;line-height:1.3}
.news-card p{position:absolute;left:20px;width:240px;font-size:10px;line-height:1.5}
.news-card .more{position:absolute;left:0;top:396px;width:100%;font-size:12px;font-weight:700}

/* practice */
.practice{top:2660px;height:689px;background:linear-gradient(180deg,#dfe7ee,var(--light-blue))}
.practice .sec-title{color:var(--navy);padding-top:104px}
.practice .rule{width:92px}
.pa-card{position:absolute;top:206px;width:280px;height:376px;background:#fff;text-align:center;box-shadow:0 2px 10px rgba(12,59,94,.08)}
.pa-card .thumb{position:absolute;left:0;top:0;width:280px;height:174px}
.pa-card .icon{position:absolute;left:108px;top:142px;width:64px;height:64px;border-radius:50%;background:var(--navy);border:3px solid #fff;display:flex;align-items:center;justify-content:center}
.pa-card h4{position:absolute;top:228px;width:100%;font-size:13px;font-weight:600;letter-spacing:.5px}
.pa-card p{position:absolute;top:254px;left:30px;width:220px;font-size:9.5px;line-height:1.45;color:var(--muted)}
.pa-card .btn{position:absolute;left:70px;top:311px;width:140px;height:32px;line-height:32px;font-size:10px;background:var(--navy)}

/* reviews */
.reviews{top:3349px;height:636px;background:#fff}
.reviews .sec-title{padding-top:100px}
.review{position:absolute;top:210px;width:212px;height:197px;background:#fff;box-shadow:0 1px 6px rgba(0,0,0,.12);padding:20px}
.review .who{display:flex;align-items:center;gap:8px}
.review .av{width:30px;height:30px;border-radius:50%;background:#c9ccd1}
.review .nm{font-size:11.5px;font-weight:700;color:var(--navy)}
.review .ago{font-size:8px;color:#999}
.review .g{position:absolute;right:12px;top:12px;width:14px;height:14px;border-radius:50%;background:#cfd8e3}
.stars{color:var(--star);font-size:13px;letter-spacing:1px;margin:8px 0 4px}
.review p{font-size:9.5px;line-height:1.55;color:var(--muted)}
.arrow{position:absolute;top:287px}
.rating{position:absolute;top:450px;width:100%;text-align:center}
.rating .score{font-size:20px;font-weight:600}
.rating .score span{color:var(--star);letter-spacing:2px}
.rating .based{font-size:9.5px;color:var(--muted);margin-top:4px}
.rating .powered{font-size:17px;margin-top:8px}
.rating .powered b{font-weight:600;color:var(--blue)}

/* share */
.share{top:3985px;height:152px;background:var(--navy)}
.share h5{position:absolute;top:34px;width:100%;text-align:center;color:#fff;font-size:15px;font-weight:700}
.share .icons{position:absolute;top:66px;left:443px;display:flex;gap:8px}
.share .icons i{width:46px;height:46px;border-radius:50%;display:block}

/* footer */
.site-footer{top:4137px;height:426px;background:var(--footer-bg);color:var(--ink)}
.f-about{position:absolute;left:163px;top:175px;width:220px;font-size:9.5px;line-height:1.55;color:#333}
.f-col{position:absolute;top:108px}
.f-col h6{font-size:15px;font-weight:700;letter-spacing:.5px;margin-bottom:22px;color:var(--navy)}
.f-col li{list-style:none;font-size:10.5px;margin-bottom:16px;color:#333}
.f-col .addr{font-size:9.5px;line-height:1.5;margin-bottom:14px;color:#333}
.copyright{position:absolute;left:0;top:4563px;width:1200px;height:52px;background:var(--navy);color:#fff;font-size:10px;text-align:center;line-height:52px}
</style>
</head>
<body>

<div class="band topbar">
  <span style="left:163px"><svg width="9" height="12" viewBox="0 0 9 12"><path d="M4.5 0C2 0 0 2 0 4.4 0 7.6 4.5 12 4.5 12S9 7.6 9 4.4C9 2 7 0 4.5 0zm0 6.2a1.8 1.8 0 110-3.6 1.8 1.8 0 010 3.6z" fill="#fff"/></svg>Location: 18 Arden Lane, Grimsby, ON L3M 2K4</span>
  <span style="left:694px"><svg width="11" height="11" viewBox="0 0 24 24"><path d="M6.6 10.8a15 15 0 006.6 6.6l2.2-2.2c.3-.3.7-.4 1-.2 1.1.4 2.3.6 3.6.6.6 0 1 .4 1 1V20c0 .6-.4 1-1 1A17 17 0 013 4c0-.6.4-1 1-1h3.5c.6 0 1 .4 1 1 0 1.3.2 2.5.6 3.6.1.3 0 .7-.2 1z" fill="#fff"/></svg>Phone: 416.555.0142</span>
  <span style="left:855px"><svg width="11" height="9" viewBox="0 0 12 9"><rect width="12" height="9" rx="1" fill="#fff"/><path d="M0 0l6 5 6-5" stroke="#082a45" fill="none"/></svg>Email: contact@dorvantlegal.ca</span>
</div>

<header class="site-header">
  <div class="logo abs" style="left:163px;top:24px"><div class="mark"></div><div class="name">DORVANT<br>LEGAL</div></div>
  <nav class="nav"><span>Practice Areas</span><span>About</span><span>News or News Articles</span><span>Resources or Legal Resources</span><span>Contact</span></nav>
  <div class="search">Search...</div>
</header>

<section class="hero">
  <div class="hero-deco" role="img" aria-label="Faint technology network graphic"></div>
  <div class="hero-photo" role="img" aria-label="Portrait photo of the lead lawyer in a suit"></div>
  <div class="hero-copy">
    <div class="kicker">WINNING.</div>
    <h1>MY CLIENTS<br>DEPEND ON ME FOR IT.<br>SHOULDN'T YOU?</h1>
  </div>
  <span class="btn btn-read">READ MORE</span>
  <span class="btn btn-video">VIDEO LIBRARY</span>
  <div class="dots"><i></i><i class="on"></i><i></i></div>
  <svg class="abs" style="left:0;top:380px" width="1200" height="173" viewBox="0 0 1200 173"><path d="M0 70 C120 150 260 130 420 120 L1200 120 L1200 173 L0 173Z" fill="#0c3b5e"/></svg>
</section>

<div class="band badges">
  <div class="badge-plain" style="left:225px;width:258px"></div>
  <div class="badge-plain" style="left:528px;width:180px;background:rgba(255,255,255,.85)"></div>
  <div class="badge-text">An excellent rating for a lawyer with some experience. This rating indicates the attorney is widely respected by their peers for high professional achievement and ethical standards.</div>
</div>

<svg class="abs" style="left:0;top:813px" width="1200" height="70" viewBox="0 0 1200 70"><path d="M0 0H1200V70C1050 10 900 2 700 0Z" fill="#0c3b5e"/></svg>

<section class="evaluation">
  <div style="padding-top:101px">
    <h2 class="sec-title">CASE EVALUATION</h2>
    <div class="rule"></div>
    <p class="center" style="font-size:12.5px;color:#555;margin-top:30px">Fill out this form to schedule your initial consult with our lawyers.</p>
  </div>
  <div class="form-box">
    <div class="field" style="left:66px;top:59px;width:316px;height:44px">First Name</div>
    <div class="field" style="left:396px;top:59px;width:316px;height:44px">Last Name</div>
    <div class="field" style="left:66px;top:118px;width:316px;height:44px">Email</div>
    <div class="field" style="left:396px;top:118px;width:316px;height:44px">Phone</div>
    <div class="field" style="left:66px;top:179px;width:646px;height:151px;border-radius:20px">Case Details</div>
    <div class="consent">* By using this site and/or submitting this form, I agree to the <b>Privacy Policy</b> and <b>Terms of Use.</b></div>
    <div class="send">SEND</div>
  </div>
</section>

<section class="experience">
  <div class="exp-head">
    <h2>YOUR EXPERIENCED<br>TORONTO AND HAMILTON LAWYERS</h2>
    <h3>GETTING THE RESULTS THAT MATTER</h3>
  </div>
  <div class="exp-rule"></div>
  <div class="exp-copy">
    <p>Dorvant Legal is a boutique litigation firm with law offices in Toronto and Hamilton. We concentrate our legal practice on complex business litigation, professional negligence (malpractice) claims, and insurance coverage disputes. We take an innovative approach to our client's legal problems, and are guided by the philosophy that our job is to get results.</p>
    <p>The lawyers at Dorvant Legal have the reputation for vigorously representing their clients' interests and competing hard to obtain the best possible results. With experience at all stages of legal disputes, the lawyers at Dorvant Legal are equally at home negotiating in a boardroom or presenting a case at trial. We hope that you take the time to explore our website to find out how our record of excellence, dedication and many years of experience can assist you.</p>
  </div>
  <article class="news-card" style="left:163px">
    <div class="thumb" role="img" aria-label="Photo of an empty courtroom with gold curtains" style="background:linear-gradient(90deg,#8a6a2a,#c9a45a 40%,#e9e6df 70%,#2c3136)"></div>
    <div class="date">April 7, 2020</div>
    <h4>Metro Wire Story on Technology in the Courts</h4>
    <p style="top:282px">Clara Vesnik interviewed the Chief Justice of Ontario along with Dorvant Lesage on the efforts by the Ontario court system to modernize in the face of Covid-19.</p>
    <div class="more">Click here...</div>
  </article>
  <article class="news-card" style="left:460px">
    <div class="thumb" role="img" aria-label="Portrait photo of the lead lawyer" style="background:radial-gradient(ellipse at 50% 45%,#6b6f74,#2b2f34)"></div>
    <div class="date">27 Nov 2023</div>
    <h4>Court denies former bencher's request for civil trial data that would show extent of court delays</h4>
    <p style="top:327px">Read about the Superior Court decision, denying Dorvant's request for basic court data</p>
    <div class="more">Click here...</div>
  </article>
  <article class="news-card" style="left:758px">
    <div class="thumb" role="img" aria-label="Illustration of a queue ticket dispenser and a now serving display" style="background:linear-gradient(135deg,#d9d6d2,#9a9fa6 60%,#4b3a3c)"></div>
    <div class="date">8 Nov 2023</div>
    <h4>In Small Claims Court, Justice Delayed</h4>
    <p style="top:272px">Dorvant is quoted in Rowan Pell's November 8, 2023 article, which you can find here.</p>
    <div class="more">Click here...</div>
  </article>
  <svg class="abs" style="left:0;top:904px" width="1200" height="90" viewBox="0 0 1200 90"><path d="M0 90V0C150 75 320 90 520 90Z" fill="#dfe7ee"/></svg>
</section>

<section class="practice">
  <h2 class="sec-title">PRACTICE AREAS</h2>
  <div class="rule"></div>
  <div class="pa-card" style="left:163px">
    <div class="thumb" role="img" aria-label="Photo of a judge's gavel in a business meeting" style="background:linear-gradient(135deg,#8a8d92,#3c3f44)"></div>
    <div class="icon"><svg width="30" height="26" viewBox="0 0 30 26" fill="none" stroke="#fff" stroke-width="2"><path d="M15 2V24M8 24H22M4 6H26M4 6L0 15H8ZM26 6L22 15H30Z"/></svg></div>
    <h4>BUSINESS LITIGATION</h4>
    <p>Business disputes can have a serious impact upon your company's bottom line.</p>
    <span class="btn">VIEW DETAILS</span>
  </div>
  <div class="pa-card" style="left:460px">
    <div class="thumb" role="img" aria-label="Photo of professionals in a tense meeting" style="background:linear-gradient(135deg,#b9b6b2,#4a4d52)"></div>
    <div class="icon"><svg width="26" height="26" viewBox="0 0 26 26" fill="#fff"><circle cx="13" cy="8" r="6"/><path d="M2 26C2 18 7 15 13 15S24 18 24 26Z"/></svg></div>
    <h4>PROFESSIONAL NEGLIGENCE</h4>
    <p>When a professional has let you down, the impact can be devastating. I have the experience need to help.</p>
    <span class="btn">VIEW DETAILS</span>
  </div>
  <div class="pa-card" style="left:758px">
    <div class="thumb" role="img" aria-label="Photo of a consultation between two people at a desk" style="background:linear-gradient(135deg,#d8d4cc,#6d6a66)"></div>
    <div class="icon"><svg width="24" height="28" viewBox="0 0 24 28"><path d="M12 0L24 5V13C24 20 18 26 12 28 6 26 0 20 0 13V5Z" fill="#fff"/><path d="M7 14l4 4 7-8" stroke="#0c3b5e" stroke-width="2.5" fill="none"/></svg></div>
    <h4>INSURANCE</h4>
    <p>When your insurance company refuses to pay, you need a lawyer who has experience suing insurance companies, and winning</p>
    <span class="btn">VIEW DETAILS</span>
  </div>
</section>

<section class="reviews">
  <h2 class="sec-title">REVIEWS</h2>
  <div class="rule" style="width:62px"></div>
  <svg class="arrow" style="left:78px" width="16" height="32" viewBox="0 0 16 32"><path d="M14 2L2 16 14 30" stroke="#444" stroke-width="2" fill="none"/></svg>
  <svg class="arrow" style="left:1105px" width="16" height="32" viewBox="0 0 16 32"><path d="M2 2L14 16 2 30" stroke="#0c3b5e" stroke-width="2" fill="none"/></svg>
  <div class="review" style="left:163px"><i class="g"></i><div class="who"><div class="av"></div><div><div class="nm">JHON DOE</div><div class="ago">4 months ago</div></div></div><div class="stars">★★★★★</div><p>Lorem ipsum dolor amet consectetr adipiscing elit sed do eiumod tempor incididunt ut labore et dolore magna aliqua. quis ipsum suspendisse ultrics gravida risus comodo.</p></div>
  <div class="review" style="left:383px"><i class="g"></i><div class="who"><div class="av"></div><div><div class="nm">JHON DOE</div><div class="ago">4 months ago</div></div></div><div class="stars">★★★★★</div><p>Lorem ipsum dolor amet consectetr adipiscing elit sed do eiumod tempor incididunt ut labore et dolore magna aliqua. quis ipsum suspendisse ultrics gravida risus comodo.</p></div>
  <div class="review" style="left:604px"><i class="g"></i><div class="who"><div class="av"></div><div><div class="nm">JHON DOE</div><div class="ago">4 months ago</div></div></div><div class="stars">★★★★★</div><p>Lorem ipsum dolor amet consectetr adipiscing elit sed do eiumod tempor incididunt ut labore et dolore magna aliqua. quis ipsum suspendisse ultrics gravida risus comodo.</p></div>
  <div class="review" style="left:825px"><i class="g"></i><div class="who"><div class="av"></div><div><div class="nm">JHON DOE</div><div class="ago">4 months ago</div></div></div><div class="stars">★★★★★</div><p>Lorem ipsum dolor amet consectetr adipiscing elit sed do eiumod tempor incididunt ut labore et dolore magna aliqua. quis ipsum suspendisse ultrics gravida risus comodo.</p></div>
  <div class="rating">
    <div class="score">4.9 <span>★★★★★</span></div>
    <div class="based">Based On 185 Reviews</div>
    <div class="powered">Powered By <b>ReviewHub</b></div>
  </div>
  <svg class="abs" style="left:0;top:546px" width="1200" height="90" viewBox="0 0 1200 90"><path d="M1200 0C1100 60 950 90 700 90H1200Z" fill="#0c3b5e"/></svg>
</section>

<section class="share">
  <h5>SHARE THIS PAGE:</h5>
  <div class="icons" aria-label="Share buttons">
    <i style="background:#3b5998"></i><i style="background:#444"></i><i style="background:#d6249f"></i><i style="background:#0a66c2"></i><i style="background:#e60023"></i><i style="background:#25a244"></i>
  </div>
</section>

<footer class="site-footer">
  <svg class="abs" style="left:0;top:0" width="1200" height="70" viewBox="0 0 1200 70"><path d="M0 0H520C300 10 120 30 0 70Z" fill="#0c3b5e"/></svg>
  <div class="logo abs" style="left:163px;top:123px"><div class="mark"></div><div class="name">DORVANT<br>LEGAL</div></div>
  <p class="f-about">Dorvant Legal is a boutique law office concentrating in Complex Business Litigation, Professional Negligence, and Insurance Coverage Disputes. Our innovative and pugnacious approach gets results for our clients in the Greater Toronto Area.</p>
  <div class="f-col" style="left:458px"><h6>LINKS</h6><ul><li>Practice Areas</li><li>About</li><li>News or News Articles</li><li>Resources or Legal<br>Resources</li><li>Contact</li></ul></div>
  <div class="f-col" style="left:663px"><h6>PRACTICE AREAS</h6><ul><li>BUSINESS LITIGATION</li><li>PROFESSIONAL NEGLIGENCE</li><li>INSURANCE</li></ul></div>
  <div class="f-col" style="left:903px"><h6>CONTACT</h6>
    <p class="addr"><b>HAMILTON OFFICE:</b><br>42 Carden Street, Ground<br>Floor Hamilton, ON L8N 2B7</p>
    <p class="addr"><b>Toronto Office:</b><br>250 Bay Row #1400,<br>Toronto, ON M5J 2R8</p>
    <p class="addr">PHONE:<br><span style="font-size:11px">416 555 0142</span></p>
  </div>
</footer>
<div class="copyright">© 2023 Dorvant Legal. All Rights Reserved.</div>

</body>
</html>
```